Business card with professional look

I would like a creative yet professional looking business card for our business. We sell broadcast TV related security products for mobile phones, set top boxes, and tablets. Our customers are international. We have a logo we like and I would like to possibly add some color to the business card but keep it professional looking.

Target Market(s)

Professionals in the TV, cable, ans Satellite industries

Industry/Entity Type

Cable Tv

Contact Information for Business Card

Name Tom Verhanic, title CEO, Address 8160 Marbury Crescent, Suite 300, La Jolla, CA 91584 USA, phone numbers m:+1.619.472.3014 o:+1.855.263.9042, email, logo

Font styles to use
Other font styles liked:
• Open to any font that looks good with logo

Requirements
Must have
• professional look with colors coordinated with logo colors. would like to add one or two different colors as well as some form of background color

```html
<!DOCTYPE html>
<html lang="en">
<head>
<meta charset="utf-8">
<title>Vaultcast Business Card</title>
<link rel="stylesheet" href="https://fonts.googleapis.com/css2?family=Source+Sans+3:wght@400;600;700&display=swap">
<style>
  :root {
    --backdrop: #5b4a3c;
    --card: #ffffff;
    --ink: #4a4a4a;
    --brand-blue: #0f4c97;
    --brand-blue-light: #1f86cf;
    --steel-dark: #3c3c3e;
    --steel-light: #8a8b8e;
    --logo-grey: #48484a;
  }
  * { margin: 0; padding: 0; box-sizing: border-box; }
  html, body {
    width: 1200px;
    height: 987px;
    overflow: hidden;
    background: var(--backdrop);
    font-family: "Source Sans 3", "Myriad Pro", Arial, sans-serif;
  }
  .card {
    position: absolute;
    left: 293px;
    top: 318px;
    width: 615px;
    height: 352px;
    background: var(--card);
    border-radius: 17px;
    overflow: hidden;
    box-shadow: 0 3px 8px rgba(0,0,0,0.35);
  }
  .brand {
    position: absolute;
    left: 46px;
    top: 60px;
    display: flex;
    align-items: center;
    gap: 10px;
  }
  .brand-mark {
    width: 30px;
    height: 30px;
    background: var(--brand-blue-light);
    border-radius: 4px;
  }
  .brand-name {
    font-size: 46px;
    font-weight: 700;
    color: var(--logo-grey);
    letter-spacing: -1px;
    line-height: 1;
  }
  .address {
    position: absolute;
    left: 46px;
    top: 166px;
    font-size: 16px;
    line-height: 20.5px;
    color: var(--ink);
    font-style: normal;
  }
  .contact-list {
    position: absolute;
    left: 46px;
    top: 239px;
    list-style: none;
    font-size: 16px;
    color: var(--ink);
  }
  .contact-list li {
    display: flex;
    align-items: center;
    height: 23.5px;
  }
  .contact-icon {
    width: 16px;
    height: 16px;
    margin-right: 11px;
    fill: var(--brand-blue);
  }
  .person {
    position: absolute;
    right: 56px;
    top: 211px;
    text-align: right;
  }
  .person-name {
    font-size: 23px;
    font-weight: 600;
    color: var(--brand-blue);
    line-height: 28px;
  }
  .person-title {
    font-size: 17px;
    color: var(--ink);
    line-height: 22px;
  }
  .footer-band {
    position: absolute;
    left: 0;
    bottom: 0;
    width: 615px;
    height: 40px;
  }
  .website {
    position: absolute;
    right: 34px;
    bottom: 12px;
    font-size: 16px;
    letter-spacing: 5px;
    color: #ffffff;
  }
</style>
</head>
<body>
  <div class="card">
    <div class="brand">
      <span class="brand-mark"></span>
      <span class="brand-name">Vaultcast</span>
    </div>

    <address class="address">
      8160 Marbury Crescent<br>
      Suite 300, La Jolla<br>
      CA 91584 USA
    </address>

    <ul class="contact-list">
      <li>
        <svg class="contact-icon" viewBox="0 0 16 16" aria-hidden="true"><path d="M3.2 1.5l2.4-.4 1.3 3.3-1.6 1.2c.8 1.8 2.2 3.3 4 4.2l1.3-1.6 3.3 1.4-.4 2.4c-.2.9-1 1.4-1.9 1.3C6.3 12.8 2.9 9.1 1.9 3.5c-.1-.9.4-1.8 1.3-2z"/></svg>
        +1.855.263.9042
      </li>
      <li>
        <svg class="contact-icon" viewBox="0 0 16 16" aria-hidden="true"><path d="M4.5 0h7c.8 0 1.5.7 1.5 1.5v13c0 .8-.7 1.5-1.5 1.5h-7C3.7 16 3 15.3 3 14.5v-13C3 .7 3.7 0 4.5 0zm.3 2v10.5h6.4V2H4.8zM8 13.4a.9.9 0 100 1.8.9.9 0 000-1.8z"/></svg>
        +1.619.472.3014
      </li>
      <li>
        <svg class="contact-icon" viewBox="0 0 16 16" aria-hidden="true"><path d="M1 3.5h14v9H1z M1.6 4l6.4 5 6.4-5" fill="var(--brand-blue)"/><path d="M1.6 4.2l6.4 4.8 6.4-4.8" fill="none" stroke="#fff" stroke-width="1"/></svg>
        Tom@vaultcast.tv
      </li>
    </ul>

    <div class="person">
      <div class="person-name">Tom Verhanic</div>
      <div class="person-title">CEO</div>
    </div>

    <svg class="footer-band" viewBox="0 0 615 40" aria-hidden="true">
      <defs>
        <linearGradient id="steel" x1="0" x2="1" y1="0" y2="0">
          <stop offset="0" stop-color="var(--steel-dark)"/>
          <stop offset="0.55" stop-color="var(--steel-light)"/>
          <stop offset="1" stop-color="var(--steel-dark)"/>
        </linearGradient>
        <linearGradient id="blueTab" x1="0" x2="1" y1="0" y2="0">
          <stop offset="0" stop-color="var(--brand-blue)"/>
          <stop offset="1" stop-color="var(--brand-blue-light)"/>
        </linearGradient>
      </defs>
      <rect x="0" y="22" width="370" height="18" fill="url(#steel)"/>
      <path d="M354 40 C360 10 380 1 420 1 L615 1 L615 40 Z" fill="#ffffff"/>
      <path d="M360 40 C366 14 384 5 424 5 L615 5 L615 40 Z" fill="url(#blueTab)"/>
    </svg>
    <div class="website">www.vaultcast.tv</div>
  </div>
</body>
</html>
```